Business Card Design

I'm a commercial general contractor remodel offices, hotels, health clubs and stores mostly San Francisco and the peninsula
the file I down loaded is kind of what I want I like the I beam with my company name in it, that would be fine with me but if you have better Idea will look at it you never know, I'm decided to give in and change my company name to how every one knows me, I have been in business since 1991, I like the I beam logo I included one of my old card from my old company for reference for you.

Industry/Entity Type

Business

Contact Information for Business Card

BRAXO CONSTRUCTION (is my company name)
Wendell Trusk contractor, LIc 314827
4158 Garnet Row, San Bruno, California 94066
mobile, (415) 555-0147
phone (650) 555-0182
Fax, (650) 555-0183
email, braxo@braxoconstruction.example

```html
<!DOCTYPE html>
<html lang="en">
<head>
<meta charset="utf-8">
<title>Wendell Trusk – Business Card</title>
<link rel="stylesheet" href="https://fonts.googleapis.com/css2?family=Noto+Sans:wght@400;700&display=swap">
<style>
  :root {
    --card-bg: #ffffff;
    --accent-blue: #1fa8f7;
    --name-blue: #2aa7ea;
    --slate: #a6bfc7;
    --ink: #1d3447;
    --logo-blue: #2f9be6;
  }
  html, body {
    margin: 0;
    padding: 0;
    overflow: hidden;
    background: var(--card-bg);
  }
  .card {
    position: relative;
    width: 1200px;
    height: 702px;
    background: var(--card-bg);
    overflow: hidden;
    font-family: "Noto Sans", Arial, sans-serif;
    color: var(--ink);
  }
  .card__shapes {
    position: absolute;
    inset: 0;
  }
  .shape--blue { fill: var(--accent-blue); }
  .shape--slate { fill: var(--slate); }
  .company-mark {
    position: absolute;
    top: 82px;
    left: 0;
    width: 1200px;
    text-align: center;
    font-size: 44px;
    font-weight: 700;
    line-height: 1;
    letter-spacing: 1px;
    color: var(--logo-blue);
  }
  .address {
    position: absolute;
    top: 190px;
    left: 0;
    width: 1200px;
    text-align: center;
    font-size: 25px;
    line-height: 30px;
  }
  .person {
    position: absolute;
    top: 303px;
    left: 0;
    width: 1200px;
    text-align: center;
  }
  .person__name {
    margin: 0;
    font-size: 66px;
    font-weight: 700;
    line-height: 1;
    color: var(--name-blue);
  }
  .person__title {
    margin: 6px 0 0;
    font-size: 36px;
    font-weight: 700;
    line-height: 1;
  }
  .contact {
    position: absolute;
    top: 460px;
    left: 0;
    width: 1200px;
    text-align: center;
    font-size: 34px;
    line-height: 45px;
  }
  .contact p { margin: 0; }
  .contact__email { font-weight: 700; }
</style>
</head>
<body>
  <div class="card">
    <svg class="card__shapes" width="1200" height="702" viewBox="0 0 1200 702" aria-hidden="true">
      <polygon class="shape--blue" points="0,17 295,246 124,670 0,664"/>
      <polygon class="shape--slate" points="1106,17 1200,28 1200,702 1172,702 891,424"/>
    </svg>

    <div class="company-mark">BRAXO CONSTRUCTION</div>

    <div class="address">4158 Garnet Row, San Bruno, California 94066</div>

    <div class="person">
      <h1 class="person__name">Wendell Trusk</h1>
      <p class="person__title">Contractor, LIc 314827</p>
    </div>

    <div class="contact">
      <p>mobile: (415) 555-0147</p>
      <p>phone: (650) 555-0182 ; Fax: (650) 555-0183</p>
      <p class="contact__email">braxo@braxoconstruction.example</p>
    </div>
  </div>
</body>
</html>
```